Book Cover "Venice"

Creation of a cover (14 x 20.5 cm + bleed area) for a book:
Image: “BrumeVerte” (Tiff joined)
AUTHOR: Corinne Valmer
TITLE: The murmurs of Lorient
PUBLISHER: Editions Pluvane (AT THE BOTTOM OF THE COVER)

Target Market(s)

Readers of romantic novels

Industry/Entity Type

Book

```html
<!DOCTYPE html>
<html lang="en">
<head>
<meta charset="utf-8">
<title>The murmurs of Lorient — Corinne Valmer</title>
<link href="https://fonts.googleapis.com/css2?family=Bebas+Neue&family=Oswald:wght@500;700&display=swap" rel="stylesheet">
<style>
  :root {
    --backdrop: #e4e4e4;
    --sky-top: #3a0508;
    --sky-mid: #c8161d;
    --sky-glow: #e02a22;
    --city-dark: #0c0507;
    --cream: #eee8cf;
  }
  html, body {
    margin: 0;
    width: 1200px;
    height: 1200px;
    overflow: hidden;
    background: var(--backdrop);
  }
  h1, p { margin: 0; }
  .cover {
    position: absolute;
    left: 225px;
    top: 50px;
    width: 750px;
    height: 1100px;
    overflow: hidden;
    box-shadow: 0 10px 30px rgba(0,0,0,0.18);
  }
  .cover-photo {
    position: absolute;
    inset: 0;
    background:
      radial-gradient(ellipse at 60% 55%, var(--sky-glow) 0%, rgba(224,42,34,0) 55%),
      linear-gradient(180deg, var(--sky-top) 0%, var(--sky-mid) 22%, var(--sky-mid) 58%, #5a0a0c 72%, var(--city-dark) 84%, var(--city-dark) 100%);
  }
  .title {
    position: absolute;
    left: 0;
    right: 0;
    top: 80px;
    text-align: center;
    color: var(--cream);
    font-family: "Bebas Neue", "Oswald", sans-serif;
    font-weight: 400;
    line-height: 0.86;
  }
  .title-article {
    display: flex;
    align-items: center;
    justify-content: center;
    gap: 22px;
    font-size: 64px;
    margin-bottom: 14px;
  }
  .title-article .rule {
    width: 250px;
    height: 2px;
    background: var(--cream);
  }
  .title-main {
    display: block;
    font-size: 232px;
    letter-spacing: -2px;
  }
  .title-link {
    display: block;
    font-size: 64px;
    margin: 8px 0 6px;
  }
  .author {
    position: absolute;
    left: 0;
    right: 0;
    top: 925px;
    text-align: center;
    color: var(--cream);
    font-family: "Oswald", sans-serif;
    font-weight: 700;
    font-size: 48px;
    line-height: 1;
    letter-spacing: 10px;
    text-transform: uppercase;
  }
  .publisher {
    position: absolute;
    left: 0;
    right: 0;
    top: 992px;
    text-align: center;
    color: var(--cream);
    font-family: "Oswald", sans-serif;
    font-weight: 500;
    font-size: 17px;
    line-height: 1;
    letter-spacing: 3px;
    text-transform: uppercase;
  }
</style>
</head>
<body>
  <main class="cover">
    <div class="cover-photo" role="img" aria-label="BrumeVerte photograph: red sunset sky over a domed church skyline silhouette with glowing street lanterns along the waterfront"></div>
    <h1 class="title">
      <span class="title-article"><span class="rule"></span>THE<span class="rule"></span></span>
      <span class="title-main">MURMURS</span>
      <span class="title-link">OF</span>
      <span class="title-main">LORIENT</span>
    </h1>
    <p class="author">Corinne Valmer</p>
    <p class="publisher">Editions Pluvane</p>
  </main>
</body>
</html>
```